Organic All Natural Gluten Free Dog Treat company needs a Design for our Label/Packaging.

We are a start up company making organic all natural gluten free dog biscuits. We are looking for a catchy label design that will impress upon first sight. Colors can be almost anything, some to consider are green, blue, white, beige, Black, Burgundy. We will be running a high class, high end business and really need to see concepts that reflect this. We are not really looking for anything comical or fun, however it needs to be nice to look at and look to be high end quality. The photo's that I have attached are what we like from other companies, these are just to throw around and maybe get ideas from. Our labels will be either 4" wide x 5" high or 5" wide x 6" high.
Updates

Project Deadline Extended Reason: We wish to extend 5 days as we would like to see more designs. Added Tuesday, July 7, 2015

Project Deadline Extended
Reason: Need more designs to make final decision.

Target Market(s)

Anyone who owns dog's or dog lover's.

Industry/Entity Type

It Company

Font styles to use
Serif
Sans Serif
Decorative
Script

Requirements
Must have
• "Stay Close Alwaystime" is the name of our business so it needs to be included,
• All Natural Organic Dog Treats...Gluten Free, No Preservatives, No Wheat, No Soy, Corn, or GMO's, Nothing Artificial, Baked by Stay Close AlwaysTime LLC., Dallas, TX.
• 6 oz., made in U.S.A.
• We don't need to use the logo, as long as the words "Stay Close AlwaysTime" are included.
Nice to have
• Not sure what colors we want, we would like to see a variety which can include brown, blue, black, green, red, yellow, orange, purple, beige, burgundy, white color scheme?? Maybe white or brownish, blueish background? American flag.
• We have uploaded a photo tilted American Eskimo Puppies for Label, we would like to have this included if possible. We have 4 flavors, Peanut Butter N' Honey, Pumpkin N' Spice, Sweet Potato, and Blueberry N' Coconut, maybe you can add the name and color code for one of these.

```html
<!DOCTYPE html>
<html lang="en">
<head>
<meta charset="utf-8">
<title>Stay Close Alwaystime – Organic Dog Treats Label</title>
<link rel="stylesheet" href="https://fonts.googleapis.com/css2?family=Arvo:wght@700&family=Playball&family=Roboto+Condensed:wght@400&family=Roboto:wght@400&display=swap">
<style>
  :root {
    --paper: #e6e7e8;
    --bark: #4f3d30;
    --meadow: #6b7a35;
    --grass-light: #8fae4c;
    --grass-dark: #4e7128;
    --cream: #ffffff;
  }
  html, body {
    margin: 0;
    padding: 0;
    overflow: hidden;
    background: var(--paper);
  }
  .label {
    position: relative;
    width: 944px;
    height: 1200px;
    background: var(--paper);
    overflow: hidden;
  }
  .hero-photo {
    position: absolute;
    left: 0;
    top: 228px;
    width: 944px;
    height: 406px;
    background: linear-gradient(180deg, var(--grass-light) 0%, #7a9c3d 45%, var(--grass-dark) 100%);
  }
  .brand-block {
    position: absolute;
    left: 301px;
    top: 4px;
    width: 334px;
    height: 255px;
    background: var(--bark);
    display: flex;
    flex-direction: column;
    align-items: center;
    justify-content: center;
    gap: 10px;
  }
  .brand-mark {
    width: 26px;
    height: 26px;
    background: var(--cream);
    margin-bottom: 8px;
  }
  .brand-name {
    font-family: "Arvo", serif;
    font-weight: 700;
    color: var(--cream);
    text-align: center;
    line-height: 1.15;
    margin: 0;
  }
  .brand-name .line-1 { display: block; font-size: 40px; letter-spacing: 1px; }
  .brand-name .line-2 { display: block; font-size: 34px; letter-spacing: 2px; }
  .natural-tag {
    position: absolute;
    left: 312px;
    top: 574px;
    width: 334px;
    height: 85px;
    background: var(--bark);
    color: var(--cream);
    font-family: "Playball", cursive;
    font-size: 44px;
    display: flex;
    align-items: center;
    justify-content: center;
  }
  .product-title {
    position: absolute;
    left: 0;
    top: 688px;
    width: 944px;
    margin: 0;
    text-align: center;
    font-family: "Arvo", serif;
    font-weight: 700;
    color: var(--bark);
  }
  .product-title .main { display: block; font-size: 92px; line-height: 100px; letter-spacing: 2px; }
  .product-title .sub { display: block; font-size: 58px; line-height: 74px; letter-spacing: 2px; }
  .claims-band {
    position: absolute;
    left: 0;
    top: 902px;
    width: 944px;
    height: 154px;
    background: var(--meadow);
    display: flex;
    align-items: center;
    justify-content: center;
  }
  .claims {
    margin: 0;
    color: var(--cream);
    font-family: "Roboto Condensed", sans-serif;
    font-size: 31px;
    line-height: 48px;
    text-align: center;
  }
  .maker-block {
    position: absolute;
    left: 304px;
    top: 1056px;
    width: 338px;
    height: 144px;
    background: var(--bark);
    color: var(--cream);
    font-family: "Roboto", sans-serif;
    text-align: center;
  }
  .maker-block .baked { position: absolute; left: 0; right: 0; top: 28px; font-size: 19px; }
  .maker-block .maker { position: absolute; left: 0; right: 0; top: 66px; font-size: 17px; letter-spacing: 0.3px; }
</style>
</head>
<body>
<main class="label">
  <div class="hero-photo" role="img" aria-label="Photo of four white fluffy puppies running in a row across a green lawn"></div>

  <header class="brand-block">
    <span class="brand-mark"></span>
    <h1 class="brand-name"><span class="line-1">STAY CLOSE</span><span class="line-2">ALWAYSTIME</span></h1>
  </header>

  <div class="natural-tag">All Natural</div>

  <h2 class="product-title">
    <span class="main">ORGANIC</span>
    <span class="sub">DOG TREATS</span>
  </h2>

  <section class="claims-band">
    <p class="claims">GRAIN &amp; GLUTEN FREE, NO PRESERVATIVES, NO SOY,<br>CORN, OR GMO'S, NOTHING ARTIFICIAL,</p>
  </section>

  <footer class="maker-block">
    <span class="baked">Baked by</span>
    <span class="maker">STAY CLOSE ALWAYSTIME LLC</span>
  </footer>
</main>
</body>
</html>
```